Stationary
Vela Rigs
Use same font as used in my logo
Use a complement to the logo font
Professional
Tom Baxter
Owner/Installation Consultant
5678 Halloway Dr.
Clark ON, K7P 5R9
tom@velarigs.com
www.velarigs.com

```html
<!DOCTYPE html>
<html lang="en">
<head>
<meta charset="utf-8">
<title>Vela Rigs — Business Cards</title>
<link rel="stylesheet" href="https://fonts.googleapis.com/css2?family=Michroma&display=swap">
<style>
  :root {
    --page: #e4e6e8;
    --black: #0b0b0c;
    --black-soft: #1c1d1f;
    --steel-light: #a9acb0;
    --steel-dark: #55585c;
    --red: #c1121c;
    --red-dark: #6e0a10;
    --text-light: #e9eaec;
    --text-mid: #9a9da1;
    --text-dark: #141516;
  }
  * { margin: 0; padding: 0; box-sizing: border-box; }
  html, body {
    width: 1200px; height: 1009px; overflow: hidden;
    background: var(--page);
    font-family: "Michroma", sans-serif;
  }
  .sheet {
    width: 1200px; height: 1009px;
    display: flex; flex-direction: column; align-items: center;
    justify-content: center; gap: 48px;
  }
  .card {
    position: relative; width: 800px; height: 457px;
    border-radius: 24px; overflow: hidden;
    box-shadow: 0 10px 26px rgba(0,0,0,.22);
  }
  .card-art { position: absolute; inset: 0; width: 100%; height: 100%; }

  /* back */
  .card--back { background: linear-gradient(160deg, var(--black-soft), var(--black) 60%); }
  .back-web {
    position: absolute; left: 40px; top: 40px;
    color: var(--text-mid); font-size: 13px; letter-spacing: .28em; text-transform: uppercase;
  }

  /* wordmark */
  .wordmark {
    position: absolute; display: flex; align-items: center; gap: 14px;
    color: var(--text-light); font-size: 30px; letter-spacing: .12em; text-transform: uppercase;
    white-space: nowrap;
  }
  .wordmark-dot { width: 18px; height: 18px; border-radius: 50%; background: var(--red); }
  .card--back .wordmark { left: 380px; top: 200px; }
  .card--front .wordmark { left: 400px; top: 120px; }

  /* front */
  .contact {
    position: absolute; left: 32px; top: 210px; list-style: none;
    color: var(--text-light); font-size: 12.5px; letter-spacing: .06em; line-height: 26px;
  }
  .contact li { display: flex; align-items: center; gap: 10px; }
  .contact-icon {
    width: 14px; height: 14px; border-radius: 50%; background: var(--text-light);
    flex: none; display: flex; align-items: center; justify-content: center;
  }
  .contact-icon svg { width: 8px; height: 8px; fill: var(--steel-dark); }
  .signature {
    position: absolute; right: 40px; bottom: 30px; text-align: right;
    color: var(--text-dark); text-transform: uppercase; letter-spacing: .14em;
  }
  .signature-name { font-size: 15px; }
  .signature-title { font-size: 11px; margin-top: 6px; }
</style>
</head>
<body>
<main class="sheet">

  <section class="card card--back">
    <svg class="card-art" viewBox="0 0 800 457" aria-hidden="true">
      <path d="M0,457 C260,420 560,340 800,250 L800,262 C560,352 260,432 0,470 Z" fill="var(--red-dark)" opacity=".5"/>
    </svg>
    <p class="back-web">www.velarigs.com</p>
    <div class="wordmark"><span class="wordmark-dot"></span>Vela Rigs</div>
  </section>

  <section class="card card--front">
    <svg class="card-art" viewBox="0 0 800 457" aria-hidden="true">
      <defs>
        <linearGradient id="steel" x1="0" y1="0" x2="1" y2="1">
          <stop offset="0" stop-color="var(--steel-dark)"/>
          <stop offset=".6" stop-color="var(--steel-light)"/>
          <stop offset="1" stop-color="var(--steel-dark)"/>
        </linearGradient>
        <linearGradient id="redband" x1="0" y1="0" x2="1" y2="1">
          <stop offset="0" stop-color="var(--red-dark)"/>
          <stop offset=".5" stop-color="var(--red)"/>
          <stop offset="1" stop-color="var(--red-dark)"/>
        </linearGradient>
      </defs>
      <rect width="800" height="457" fill="url(#steel)"/>
      <path d="M0,0 H800 V346 C520,306 260,166 0,156 Z" fill="var(--red-dark)"/>
      <path d="M0,0 H800 V336 C520,296 260,156 0,146 Z" fill="url(#redband)"/>
      <path d="M0,0 H800 V318 C520,278 260,138 0,128 Z" fill="var(--black)"/>
      <path d="M0,0 H800 V310 C520,270 260,130 0,120 Z" fill="var(--black-soft)"/>
      <path d="M0,0 H800 V300 C520,260 260,120 0,110 Z" fill="var(--black)"/>
    </svg>

    <ul class="contact">
      <li><span class="contact-icon"><svg viewBox="0 0 10 10"><path d="M5 0a3.5 3.5 0 0 0-3.5 3.5C1.5 6 5 10 5 10s3.5-4 3.5-6.5A3.5 3.5 0 0 0 5 0z"/></svg></span>5678 Halloway Dr.</li>
      <li><span class="contact-icon"><svg viewBox="0 0 10 10"><path d="M5 0a3.5 3.5 0 0 0-3.5 3.5C1.5 6 5 10 5 10s3.5-4 3.5-6.5A3.5 3.5 0 0 0 5 0z"/></svg></span>Clark ON, K7P 5R9</li>
      <li><span class="contact-icon"><svg viewBox="0 0 10 10"><path d="M2 0h2l1 3-1.5 1a6 6 0 0 0 2.5 2.5L7 5l3 1v2c0 1-1 2-2 2C4 10 0 6 0 2c0-1 1-2 2-2z"/></svg></span>555-014-2290</li>
      <li><span class="contact-icon"><svg viewBox="0 0 10 10"><path d="M0 2h10v6H0z M0 2l5 3.5L10 2"/></svg></span>tom@velarigs.com</li>
      <li><span class="contact-icon"><svg viewBox="0 0 10 10"><circle cx="5" cy="5" r="4"/></svg></span>www.velarigs.com</li>
    </ul>

    <div class="wordmark"><span class="wordmark-dot"></span>Vela Rigs</div>

    <div class="signature">
      <p class="signature-name">Tom Baxter</p>
      <p class="signature-title">Owner/Installation Consultant</p>
    </div>
  </section>

</main>
</body>
</html>
```